Pellmar Drones webdesign: Innovative Drones service company in agriculture

We need a new website according the following conditions:
• Main colour orange and current logo;
• Transparent – open – trustworthy – dynamic - personal;
• Use the smartness and overview characteristics of the crow (Pellmar is Latin for crow);
• Accessible to multiple target groups and markets:
o So not too horticultural, too green;
• Use contradictions:
o Future versus nostalgia;
o Smartness crow versus precision hummingbird;
o Technology versus mechanical;
• Tovari 2.4 RLX as a style icon?
• Long pager website
Updates

Website menu o Home o Crop monitoring  Applications Growth | Stress | Development | Diseases  Markets Breeding | Young plant | Potplants | Cutflowers | Vegetables | Soft fruit  Customer cases o Technology Aerial data collection | Artificial intelligence | Free data sets o About Vision | Company | Partners | Team | Career o Contact o News&downloads Logo: www.pellmardrones-example.com

Target Market(s)

agriculture: owners, crop managers
oil&gas: maintenance, quality control managers and purchase managers
logistics: ware house managers, purchase managers

Industry/Entity Type

Agribusiness

Number of Pages Required

2 page

Colors
f78f20

Requirements
Must have
• long pager website
downloads
LinkedIn
Should not have
• Not too 'green' because first impression of designers of agriculture/horticulture is using the green colour. But that is not necessary.

Keep in mind that the current logo will be updates: the circle will be more 'general' and less 'agri'. Also the green colors in the logo will be slightly darker to make it more powerful.

```html
<!DOCTYPE html>
<html lang="en">
<head>
<meta charset="utf-8">
<title>Pellmar Drones</title>
<link href="https://fonts.googleapis.com/css2?family=Poppins:wght@400;500;600;700;800&display=swap" rel="stylesheet">
<style>
:root{
  --orange:#f78f20;
  --navy:#1c2a40;
  --navy-deep:#1e2a3e;
  --ink:#1f2a3a;
  --muted:#8a8f98;
  --light:#f2f3f6;
  --field:#f3f4f7;
  --white:#ffffff;
}
*{margin:0;padding:0;box-sizing:border-box}
html,body{width:1200px;height:3514px;overflow:hidden}
body{font-family:'Poppins',sans-serif;color:var(--ink);background:var(--white);position:relative}
.abs{position:absolute}

/* header */
.site-header{position:absolute;left:0;top:0;width:1200px;height:111px;background:var(--white)}
.brand{position:absolute;display:flex;align-items:center;gap:12px}
.brand-dot{width:52px;height:52px;border-radius:50%;background:var(--orange)}
.brand-name{font-family:'Poppins',sans-serif;font-weight:600;color:var(--orange);font-size:25px;letter-spacing:1px;line-height:1}
.main-nav{position:absolute;left:375px;top:54px;display:flex;font-size:13px;font-weight:500;color:var(--ink)}
.main-nav span{margin-right:31px;display:flex;align-items:center;gap:4px}
.main-nav svg{width:8px;height:8px}
.lang{position:absolute;left:1070px;top:44px;width:72px;height:32px;border:1px solid #333;font-size:12px;font-weight:600;display:flex;align-items:center;justify-content:center;gap:6px}
.lang i{display:block;width:18px;height:12px;background:linear-gradient(#c8102e 50%,#3c5aa6 50%)}

/* hero */
.hero{position:absolute;left:0;top:111px;width:1200px;height:530px;background:linear-gradient(100deg,#4b4e3c 0%,#3f5a2e 30%,#6a4a3a 55%,#4c5e33 75%,#7a3b3a 100%)}
.hero-text{position:absolute;right:58px;top:170px;text-align:right;color:var(--white)}
.hero-text h1{font-weight:800;font-size:52px;line-height:58px}
.hero-text h1 em{font-style:normal;color:var(--orange)}
.hero-text p{font-size:26px;font-weight:400;margin-top:4px}
.call-btn{position:absolute;left:925px;top:453px;width:217px;height:48px;background:var(--orange);color:var(--white);font-size:20px;display:flex;align-items:center;justify-content:center;gap:12px}

/* feature cards */
.features{position:absolute;left:137px;top:596px;width:1025px;height:338px;display:flex}
.feature{flex:1;background:var(--white);box-shadow:0 4px 18px rgba(0,0,0,.08);text-align:center;padding-top:37px}
.feature-icon{width:72px;height:72px;background:var(--orange);margin:0 auto;display:flex;align-items:center;justify-content:center}
.feature h3{font-size:18px;font-weight:500;line-height:25px;margin-top:18px}
.feature p{font-size:13px;color:var(--muted);line-height:25px;margin:14px auto 0;width:280px}
.feature a{display:block;font-size:11px;font-weight:600;color:var(--orange);margin-top:8px;text-decoration:none}

/* what we do */
.wwd-photo{position:absolute;left:0;top:991px;width:581px;height:547px;background:linear-gradient(180deg,#c9ced3 0%,#a5b1a6 30%,#5d8a45 55%,#4a7a36 80%,#2f3a33 100%)}
.wwd-panel{position:absolute;left:482px;top:1038px;width:718px;height:447px;background:var(--navy);color:var(--white);padding:38px 58px 0 48px}
.wwd-panel h2{font-size:23px;font-weight:500;border-left:3px solid var(--orange);padding-left:14px;line-height:32px}
.wwd-panel p{font-size:16.4px;line-height:22px;color:#c7ccd4;text-align:justify;margin-top:32px}
.wwd-rule{height:1px;background:#3a475c;margin-top:42px}
.pains{display:flex;gap:0;margin-top:45px;margin-left:11px}
.pains span{width:122px;height:35px;background:var(--orange);font-size:16px;display:flex;align-items:center;justify-content:center}
.pains span+span{margin-left:19px}
.pains span:nth-child(3){margin-left:24px;width:145px}
.pains span:nth-child(4){margin-left:28px}

/* steps */
.steps-section{position:absolute;left:0;top:1540px;width:1200px;height:624px;background:var(--light);text-align:center}
.eyebrow{font-size:12px;letter-spacing:1px;color:var(--muted);margin-top:82px}
.steps-section h2{font-size:34px;font-weight:500;margin-top:6px}
.steps-section .bar{width:64px;height:4px;background:var(--orange);margin:10px auto 0}
.step{position:absolute;top:225px;width:240px;text-align:center}
.step-photo{width:176px;height:176px;border-radius:50%;margin:0 auto;position:relative}
.step-num{position:absolute;right:0;top:-5px;width:42px;height:42px;border-radius:50%;background:var(--navy);color:var(--white);font-size:17px;font-weight:500;display:flex;align-items:center;justify-content:center;border:3px solid var(--light)}
.step h4{color:var(--orange);font-size:18px;font-weight:500;line-height:22px;margin-top:22px}
.step p{font-size:13px;color:#444;line-height:18px;margin-top:10px}

/* video band */
.video-band{position:absolute;left:0;top:2164px;width:1200px;height:510px;background:linear-gradient(180deg,#3a4352 0%,#4a5260 40%,#303845 100%)}
.play{position:absolute;left:556px;top:89px;width:88px;height:88px;border-radius:50%;background:rgba(247,143,32,.35);display:flex;align-items:center;justify-content:center}
.play b{width:64px;height:64px;border-radius:50%;background:var(--orange);display:flex;align-items:center;justify-content:center}
.video-band h5{position:absolute;top:208px;width:100%;text-align:center;color:var(--white);font-size:19px;font-weight:500}
.video-band h2{position:absolute;top:240px;width:100%;text-align:center;color:var(--white);font-size:55px;font-weight:700;line-height:46px}

/* quote */
.quote{position:absolute;left:58px;top:2552px;width:663px;height:500px;background:var(--white);padding:40px 0 0 38px}
.quote .eyebrow2{border-left:4px solid var(--orange);padding-left:22px;height:64px}
.quote .eyebrow2 small{font-size:12px;letter-spacing:1px;color:var(--muted);display:block;padding-top:2px}
.quote h2{font-size:32px;font-weight:500;line-height:40px}
.field{position:absolute;background:var(--field);font-size:12px;color:#555;padding:0 14px;display:flex;align-items:center}
.submit{position:absolute;left:38px;top:448px;width:503px;height:40px;background:var(--orange);color:var(--white);font-size:12px;font-weight:600;display:flex;align-items:center;justify-content:center}
.grow{position:absolute;left:721px;top:2552px;width:421px;height:490px;background:linear-gradient(180deg,#e3e6e9 0%,#c1c8cc 30%,#6f8c4f 60%,#3f5f2c 100%);padding:290px 0 0 26px;font-size:52px;font-weight:700;line-height:56px}
.grow .o{color:var(--orange)}.grow .w{color:var(--white)}

/* footer */
.site-footer{position:absolute;left:0;top:3106px;width:1200px;height:408px;background:var(--navy-deep);color:var(--white);text-align:center}
.site-footer .brand{left:498px;top:82px}
.contact-lines{position:absolute;top:164px;width:100%;font-size:13px;font-weight:600;line-height:22px}
.socials{position:absolute;top:253px;left:0;width:100%;display:flex;justify-content:center;gap:10px}
.socials i{width:12px;height:12px;border-radius:50%;background:#9aa3b0;display:block}
.foot-rule{position:absolute;left:62px;top:309px;width:1080px;height:1px;background:#3a465a}
.copyright{position:absolute;top:330px;width:100%;font-size:13px;color:#c2c8d0}
</style>
</head>
<body>

<header class="site-header">
  <div class="brand" style="left:68px;top:38px"><span class="brand-dot"></span><span class="brand-name">PELLMAR DRONES</span></div>
  <nav class="main-nav">
    <span>HOME</span>
    <span>CROP MONITERING <svg viewBox="0 0 8 8"><path d="M1 2l3 3 3-3" stroke="#333" fill="none"/></svg></span>
    <span>TECHNOLOGY <svg viewBox="0 0 8 8"><path d="M1 2l3 3 3-3" stroke="#333" fill="none"/></svg></span>
    <span style="margin-right:14px">ABOUT <svg viewBox="0 0 8 8"><path d="M1 2l3 3 3-3" stroke="#333" fill="none"/></svg></span>
    <span style="margin-right:22px">CONTACT</span>
    <span>NEWS &amp; DOWNLOAD</span>
  </nav>
  <div class="lang">EN <i></i><svg width="8" height="8" viewBox="0 0 8 8"><path d="M1 2l3 3 3-3" stroke="#333" fill="none"/></svg></div>
</header>

<section class="hero" role="img" aria-label="Orange drone flying over rows of flowering plants in a greenhouse">
  <div class="hero-text">
    <h1>We are <em>Always</em><br>Ready to Service</h1>
    <p>For Immediate Sevices Dial</p>
  </div>
</section>
<div class="call-btn">
  <svg width="16" height="16" viewBox="0 0 24 24"><path fill="#fff" d="M6.6 10.8a15 15 0 006.6 6.6l2.2-2.2c.3-.3.7-.4 1-.2 1.1.4 2.3.6 3.6.6.6 0 1 .4 1 1V20c0 .6-.4 1-1 1A17 17 0 013 4c0-.6.4-1 1-1h3.5c.6 0 1 .4 1 1 0 1.3.2 2.5.6 3.6.1.3 0 .7-.2 1z"/></svg>
  +31 6 55501284
</div>

<section class="features">
  <article class="feature">
    <div class="feature-icon"><svg width="40" height="30" viewBox="0 0 40 30"><path d="M4 8h12M24 8h12M10 8v4h20V8M14 12l-2 8M26 12l2 8M16 18h8" stroke="#fff" stroke-width="2.2" fill="none"/></svg></div>
    <h3>Large Number<br>of Services Provided</h3>
    <p>We are a company providing a wide range of maintenance and many other services.</p>
    <a>MORE SERVICES &nbsp;»</a>
  </article>
  <article class="feature">
    <div class="feature-icon"><svg width="36" height="30" viewBox="0 0 36 30"><rect x="2" y="7" width="32" height="21" rx="3" fill="#fff"/><rect x="12" y="2" width="12" height="7" rx="2" stroke="#fff" stroke-width="2.5" fill="none"/><rect x="15" y="14" width="6" height="4" fill="#f78f20"/></svg></div>
    <h3>10+ Years of<br>Professional Experience</h3>
    <p>We work to ensure people's comfort at their home to provide the best and the fastest.</p>
    <a>MORE ABOUT &nbsp;»</a>
  </article>
  <article class="feature">
    <div class="feature-icon"><svg width="40" height="30" viewBox="0 0 40 30"><circle cx="20" cy="8" r="6" fill="#fff"/><circle cx="8" cy="11" r="4.5" fill="#fff"/><circle cx="32" cy="11" r="4.5" fill="#fff"/><path d="M10 28c0-8 4-12 10-12s10 4 10 12zM0 26c0-6 3-9 8-9 2 0 3 1 3 1-2 3-3 5-3 8zM40 26c0-6-3-9-8-9-2 0-3 1-3 1 2 3 3 5 3 8z" fill="#fff"/></svg></div>
    <h3>A Large Number<br>of Grateful Customers</h3>
    <p>We have been working for years to improve our skills, to expand the spheres of our work.</p>
    <a>READ MORE &nbsp;»</a>
  </article>
</section>

<div class="wwd-photo" role="img" aria-label="Orange drone hovering inside a greenhouse above young green plants"></div>
<section class="wwd-panel">
  <h2>WHAT WE DO</h2>
  <p>Pellmar Drones has developed a unique autonomous drone system that is able to fly and navigate in a greenhouse without manual interference. Based on a flight plan the drone follows the right coordinates in the greenhouse, day or night, collecting high accurate data. Data is being interpreted by Artificial Intelligence software resulting in crop improvement information. The focus is the following four customer pains :</p>
  <div class="wwd-rule"></div>
  <div class="pains"><span>Growth</span><span>Stress</span><span>Development</span><span>Diseases</span></div>
</section>

<section class="steps-section">
  <p class="eyebrow">HOW IT WORKS</p>
  <h2>Follow 4 Easy Steps</h2>
  <div class="bar"></div>
  <div class="step" style="left:105px">
    <div class="step-photo" role="img" aria-label="Two colleagues reviewing a plan together" style="background:linear-gradient(135deg,#d8d2c8,#8c7a68)"><span class="step-num">01</span></div>
    <h4>Schedule your<br>Experience</h4>
    <p>He found himself transformed in<br>his bed into a horrible vermin.</p>
  </div>
  <div class="step" style="left:374px">
    <div class="step-photo" role="img" aria-label="Service advisor holding a clipboard" style="background:linear-gradient(135deg,#6f8f6a,#2f4a7a)"><span class="step-num">02</span></div>
    <h4>Get Professional<br>Advices</h4>
    <p>He found himself transformed in<br>his bed into a horrible vermin.</p>
  </div>
  <div class="step" style="left:637px">
    <div class="step-photo" role="img" aria-label="Service expert meeting a customer" style="background:linear-gradient(135deg,#8fa884,#a05060)"><span class="step-num">03</span></div>
    <h4>Meet Your Service<br>Expert</h4>
    <p>He found himself transformed in<br>his bed into a horrible vermin.</p>
  </div>
  <div class="step" style="left:900px">
    <div class="step-photo" role="img" aria-label="Orange drone inside a greenhouse" style="background:linear-gradient(180deg,#c8ccd0,#6b8a5a)"><span class="step-num">04</span></div>
    <h4>Get a Best Drone for<br>your Greenhouse</h4>
    <p>He found himself transformed in<br>his bed into a horrible vermin.</p>
  </div>
</section>

<section class="video-band" role="img" aria-label="Drone flying through a greenhouse, darkened video still">
  <div class="play"><b><svg width="22" height="24" viewBox="0 0 22 24"><path d="M3 2l17 10L3 22z" fill="#fff"/></svg></b></div>
  <h5>Don't Know What To Start With Pellmar Drones?</h5>
  <h2>Get A Solutions For All<br>Greenhouse</h2>
</section>

<section class="quote">
  <div class="eyebrow2"><small>FREE CONSULTATION</small><h2>Get a Free Quote</h2></div>
  <div class="field" style="left:38px;top:131px;width:237px;height:42px">Full Name</div>
  <div class="field" style="left:303px;top:131px;width:238px;height:42px">Email Address</div>
  <div class="field" style="left:38px;top:193px;width:237px;height:42px">Phone Number</div>
  <div class="field" style="left:303px;top:193px;width:238px;height:42px">Zip Code</div>
  <div class="field" style="left:38px;top:254px;width:503px;height:38px;justify-content:space-between">Services <svg width="8" height="8" viewBox="0 0 8 8"><path d="M1 2l3 3 3-3" stroke="#333" fill="none"/></svg></div>
  <div class="field" style="left:38px;top:312px;width:503px;height:117px;align-items:flex-start;padding-top:14px">Your Message</div>
  <div class="submit">GET A FREE QUOTE</div>
</section>
<div class="grow" role="img" aria-label="Drone above crops in a bright greenhouse"><span class="o">LETS</span><br><span class="w">GROW</span><br><span class="o">TOGETHER</span></div>

<footer class="site-footer">
  <div class="brand"><span class="brand-dot"></span><span class="brand-name">PELLMAR DRONES</span></div>
  <div class="contact-lines">
    Address: Veldzichtlaan 412, 6543KL, Lindhoven<br>
    Email: info@pellmardrones-example.com<br>
    Telephone: +31 6 55501284
  </div>
  <div class="socials" aria-label="Social media links"><i></i><i></i><i></i><i></i></div>
  <div class="foot-rule"></div>
  <p class="copyright">Copyright © 2020 Pellmar Drones . All rights reserved.</p>
</footer>

</body>
</html>
```